Design a Website Mockup for orvelHome

We are looking for someone to create our company a website mockup (psd template). Our company installs and programs home automation systems. We are looking for a professional design as our clients can spend between $60,000-$300,000 on their systems.
Our Colour Scheme is Orange and Blue and our logo is attached.
Some websites that we like include:
www.corvalhomes.com.au (Most Favourite Website)
www.pellarix.com.au

```html
<!DOCTYPE html>
<html lang="en">
<head>
<meta charset="utf-8">
<title>orvelHome – Home Automation</title>
<link href="https://fonts.googleapis.com/css2?family=Arimo:ital,wght@0,400;0,700;1,400&display=swap" rel="stylesheet">
<style>
:root{
  --blue-deep:#0b3f7a;
  --blue-mid:#1764ad;
  --blue-bright:#1f80cc;
  --blue-sky:#49a9e8;
  --blue-night:#082d5c;
  --orange:#f7941d;
  --orange-light:#fbb040;
  --orange-dark:#e07a10;
  --white:#ffffff;
  --link-blue:#49b0f0;
  --ink:#1b1b1b;
}
*{margin:0;padding:0;box-sizing:border-box}
html,body{width:1200px;height:965px;overflow:hidden}
body{
  font-family:"Arimo",Arial,sans-serif;
  background:radial-gradient(ellipse at 50% 40%,var(--blue-bright) 0%,var(--blue-mid) 45%,var(--blue-deep) 100%);
  color:var(--white);
  position:relative;
}
.site-header{position:absolute;left:0;top:0;width:1200px;height:151px}
.brand{position:absolute;left:180px;top:40px;display:flex;align-items:center;gap:14px}
.brand-dot{width:70px;height:70px;border-radius:50%;background:var(--orange)}
.brand-name{font-size:46px;font-weight:700;color:var(--white);letter-spacing:-0.5px;white-space:nowrap}
.top-links{position:absolute;right:180px;top:20px;font-size:14px;color:var(--link-blue);white-space:nowrap}
.top-links .phone{color:var(--orange-light)}
.top-links .sep{margin:0 8px;color:var(--link-blue)}
.search{position:absolute;left:727px;top:71px;width:289px;height:38px;border-radius:19px;background:var(--blue-night);
  display:flex;align-items:center;justify-content:space-between;padding:0 14px 0 18px;box-shadow:inset 0 2px 4px rgba(0,0,0,.5)}
.search span{font-style:italic;font-size:14px;color:var(--white);white-space:nowrap}
.main-nav{position:absolute;left:0;top:151px;width:1200px;height:52px;
  background:linear-gradient(var(--orange-light),var(--orange) 50%,var(--orange-dark));
  box-shadow:0 2px 4px rgba(0,0,0,.35)}
.main-nav ul{list-style:none;position:absolute;left:180px;width:843px;height:52px;display:flex;
  border-left:1px solid var(--orange-dark);border-right:1px solid var(--orange-dark)}
.main-nav li{display:flex;align-items:center;justify-content:center;font-weight:700;font-size:16px;color:var(--ink);
  border-right:1px solid var(--orange-dark);white-space:nowrap}
.main-nav li:last-child{border-right:none}
.hero-photo{position:absolute;left:0;top:203px;width:1200px;height:341px;
  background:linear-gradient(90deg,#5e5a3a 0%,#c9c58a 20%,#e1dc9c 45%,#8fa8c8 55%,#c8c48a 75%,#5f5b3c 100%)}
.hero-frame{position:absolute;left:180px;top:203px;width:843px;height:341px;border:1px solid rgba(255,255,255,.35);
  box-shadow:0 0 18px rgba(0,0,0,.6)}
.hero-caption{position:absolute;left:460px;top:431px;width:563px;height:113px;background:rgba(10,45,95,.88);
  border-left:5px solid var(--orange);padding:16px 20px}
.hero-caption h1{font-size:25px;font-weight:700;color:var(--blue-sky);margin-bottom:10px;white-space:nowrap}
.hero-caption p{font-size:13.5px;line-height:18px;color:var(--white);white-space:nowrap}
.service-card{position:absolute;top:557px;width:276px;height:259px;background:var(--blue-night);
  box-shadow:0 6px 10px rgba(0,0,0,.35)}
.service-card h2{height:47px;background:linear-gradient(#e6f5fd,#8fd0f5 40%,#2f9be0);font-size:21px;font-weight:700;
  color:var(--blue-deep);padding:12px 0 0 29px;border-left:6px solid var(--blue-sky);white-space:nowrap}
.service-photo{height:133px;background:linear-gradient(135deg,#3a2418 0%,#7a4d2e 40%,#d8c7a0 60%,#4a3020 100%)}
.service-card p{font-size:14px;line-height:17px;padding:10px 14px 0;color:var(--white);white-space:nowrap}
.service-card a{font-size:13px;color:var(--orange-light);text-decoration:underline;padding-left:14px}
.more-dots{color:var(--orange-light);font-size:13px}
.site-footer{position:absolute;left:0;top:883px;width:1200px;height:82px;
  background:linear-gradient(var(--blue-mid),var(--blue-deep));border-top:1px solid rgba(255,255,255,.15)}
.footer-links{position:absolute;left:178px;top:24px;font-size:14px;white-space:nowrap}
.footer-links .sep{margin:0 7px}
.footer-note{position:absolute;left:178px;top:49px;font-size:12px;white-space:nowrap}
.social{position:absolute;left:946px;top:18px;display:flex;gap:4px}
.social span{width:20px;height:20px;border-radius:3px;background:var(--blue-sky)}
.social span:nth-child(3){background:#c8232c}
.copyright{position:absolute;right:182px;top:49px;font-size:12.5px;white-space:nowrap}
</style>
</head>
<body>
<header class="site-header">
  <div class="brand"><div class="brand-dot"></div><span class="brand-name">orvelHome</span></div>
  <div class="top-links"><span class="phone">Call: <b>0800-555-0192</b></span><span class="sep">|</span>About Us<span class="sep">|</span>How It Works<span class="sep">|</span>Major Products</div>
  <div class="search"><span>Type here to search for devices .....</span>
    <svg width="22" height="22" viewBox="0 0 22 22"><circle cx="9" cy="9" r="6" fill="none" stroke="#f7941d" stroke-width="3"/><line x1="13.5" y1="13.5" x2="19" y2="19" stroke="#f7941d" stroke-width="3.5" stroke-linecap="round"/></svg>
  </div>
</header>
<nav class="main-nav"><ul>
  <li style="width:116px">Home</li><li style="width:157px">for Residence</li><li style="width:170px">for Commercial</li>
  <li style="width:124px">Gallery</li><li style="width:114px">Features</li><li style="width:162px">Contact Us</li>
</ul></nav>
<div class="hero-photo" role="img" aria-label="Luxury vehicle interior with a built-in screen at a showroom"></div>
<div class="hero-frame"></div>
<section class="hero-caption">
  <h1>Lorem ipsum dolor sit amet</h1>
  <p>Cnsectetur adipiscing elit. Etiam bibendum purus a orci commodo consectetur.<br>Vivamus tincidunt eros sed erat mollis v purus a orci commodo consectetur. amus</p>
</section>
<article class="service-card" style="left:177px">
  <h2>for Residence</h2>
  <div class="service-photo" role="img" aria-label="Living room with armchair, shelves and lamp"></div>
  <p>Cnsectetur adipiscing elit. Etiam biben-<br>dum purus a orci com</p><a>Read more</a> <span class="more-dots">...</span>
</article>
<article class="service-card" style="left:459px">
  <h2>for Commercial</h2>
  <div class="service-photo" role="img" aria-label="Living room with armchair, shelves and lamp"></div>
  <p>Cnsectetur adipiscing elit. Etiam biben-<br>dum purus a orci com</p><a>Read more</a> <span class="more-dots">...</span>
</article>
<article class="service-card" style="left:741px">
  <h2>for ShowRoom</h2>
  <div class="service-photo" role="img" aria-label="Living room with armchair, shelves and lamp"></div>
  <p>Cnsectetur adipiscing elit. Etiam biben-<br>dum purus a orci com</p><a>Read more</a> <span class="more-dots">...</span>
</article>
<footer class="site-footer">
  <div class="footer-links">Call: 0800-555-0192<span class="sep">|</span>Live Help<span class="sep">|</span>About Us<span class="sep">|</span>How It Works<span class="sep">|</span>Major Products</div>
  <div class="footer-note">Lorem ipsum dolor sit amet, consectetur adipiscing elit. Etiam bibendum purus a orci commodo consectetur.</div>
  <div class="social"><span></span><span></span><span></span></div>
  <div class="copyright">Copyright © All rights reserved</div>
</footer>
</body>
</html>
```